Basic images needed for business powerpoint slides

We need basic images for a powerpoint design. The designs should be clean, modern, simple and easy to read on a screen and if they were printed on paper. The images should not be overly designed (no fancy graphics or ornate fonts), but should still look professional.

Please pay attention to the attachments that have sketches of the images that are needed. In the notes section of the powerpoint slides specifies additional details for each image.

Also, please adhere to the design guidelines that are also uploaded. Only use colors and fonts that are specified. The final images should be similar to the look and feel of the images in the design guidelines.
Updates

Designers -
Thanks for all your submissions! I am reviewing all the designs with my team and will have a decision ready by Sunday evening. If you are submitting any new designs, please submit by Sunday morning EST so my team can review them.

Thanks!

Target Market(s)

business executives

Industry/Entity Type

Business

Requirements
Must have
• Must Have:
- 1. Please see the attached powerpoint for the sketches we would like to have recreated. There are specific notes in each slide with additional details.

2. Please refer to the following pages in the uploaded design guideline document:
Colors - p. 14
- Use either the bright or muted color options as specified in the color scheme on this page

Typography - p. 16-17
- Use either helvetica or arial options

Powerpoint guidelines - p.42
- see for example of the general look and feel of the company

```html
<!DOCTYPE html>
<html lang="en">
<head>
<meta charset="utf-8">
<title>Stakeholder Map – Internal and External</title>
<link href="https://fonts.googleapis.com/css2?family=Arimo:ital,wght@0,400;0,700;1,400&family=Oswald:wght@600&display=swap" rel="stylesheet">
<style>
  :root {
    --navy: #1b4f9a;
    --ring-black: #2b2b2b;
    --ring-band: #3c3c3c;
    --ring-mid: #575757;
    --slice-1: #c9c9c9;
    --slice-2: #b3b3b3;
    --slice-3: #a1a1a1;
    --slice-4: #929292;
    --pink: #d93a92;
    --green: #6dbf45;
    --teal-blue: #1a80c4;
    --card-dark: #2f2f2f;
    --ink: #222;
    --white: #fff;
    --sans: "Arimo", Arial, Helvetica, sans-serif;
    --condensed: "Oswald", "Arial Narrow", sans-serif;
  }
  * { box-sizing: border-box; margin: 0; padding: 0; }
  html, body { width: 1200px; height: 900px; overflow: hidden; background: var(--white); }
  .stage { position: relative; width: 1200px; height: 900px; font-family: var(--sans); color: var(--ink); }
  .shapes { position: absolute; left: 0; top: 0; }
  .ring-label { font-family: var(--sans); fill: var(--white); font-size: 12px; text-anchor: middle; }
  .ring-label.small { font-size: 9.5px; }

  .section-tag {
    position: absolute; top: 58px; width: 95px; height: 28px;
    background: var(--navy); color: var(--white);
    font-size: 17px; line-height: 28px; padding-left: 6px;
  }

  .num {
    position: absolute; width: 15px; height: 15px;
    background: var(--navy); color: var(--white);
    font-size: 9px; line-height: 15px; text-align: center;
  }

  .specialist {
    position: absolute; width: 62px; height: 58px;
    background: var(--navy); color: var(--white);
    padding: 4px 4px 0;
  }
  .specialist .name { font-size: 14px; font-weight: 700; line-height: 15px; }
  .specialist .role { font-size: 11.5px; line-height: 13px; }
  .specialist .scope { font-size: 7px; line-height: 8px; margin-top: 4px; }
  .specialist.tall { height: 67px; }

  .tag-box {
    position: absolute; background: var(--navy); color: var(--white);
    font-size: 11px; line-height: 11.5px; padding: 3px 4px;
  }

  .division {
    position: absolute; width: 150px; height: 51px;
    color: var(--white); text-align: center;
    font-family: var(--condensed); font-weight: 600; font-size: 17px; line-height: 46px;
    border-bottom: 5px solid var(--card-dark);
  }
  .division.medical { background: var(--pink); }
  .division.bio { background: var(--green); }

  .team { position: absolute; width: 94px; }
  .team .team-title {
    height: 20px; color: var(--white); font-size: 11px; font-weight: 700;
    line-height: 20px; padding-left: 6px;
  }
  .team .team-members {
    background: var(--card-dark); color: var(--white);
    font-size: 10px; line-height: 12px; padding: 7px 6px; height: 38px;
  }
  .team.pink .team-title { background: var(--pink); }
  .team.green .team-title { background: var(--green); }
  .team.blue .team-title { background: var(--teal-blue); }
  .team.blue .team-members { text-align: center; height: 30px; }

  .zone-label { position: absolute; font-style: italic; font-size: 15px; color: var(--ink); }
</style>
</head>
<body>
<div class="stage">

  <svg class="shapes" width="1200" height="900" viewBox="0 0 1200 900" aria-hidden="true">
    <!-- internal wheel -->
    <g class="wheel internal">
      <path d="M521.4 399.6 A212 212 0 1 0 182.6 399.6 L200.2 386.4 A190 190 0 1 1 503.8 386.4 Z" fill="var(--ring-black)"/>
      <circle cx="352" cy="272" r="190" fill="var(--navy)"/>
      <path d="M352 272 L196.4 163 A190 190 0 0 1 507.6 163 Z" fill="var(--ring-band)"/>
      <circle cx="338" cy="282" r="152" fill="var(--ring-mid)"/>
      <path d="M338 282 L219 282 A119 119 0 0 1 338 163 Z" fill="var(--slice-1)"/>
      <path d="M338 282 L338 163 A119 119 0 0 1 457 282 Z" fill="var(--slice-2)"/>
      <path d="M338 282 L457 282 A119 119 0 0 1 338 401 Z" fill="var(--slice-3)"/>
      <path d="M338 282 L338 401 A119 119 0 0 1 219 282 Z" fill="var(--slice-4)"/>
      <text class="ring-label" x="338" y="89">Franchise Lawyers | Finance</text>
      <text class="ring-label" x="338" y="118">Legal Analysts</text>
      <text class="ring-label" x="340" y="153">Sales &amp; Marketing</text>
      <text class="ring-label" x="338" y="417">Scientists</text>
      <g stroke="var(--white)" stroke-width="0.8">
        <line x1="413" y1="86" x2="422" y2="93"/>
        <line x1="380" y1="118" x2="388" y2="121"/>
        <line x1="283" y1="157" x2="290" y2="150"/>
        <line x1="365" y1="411" x2="373" y2="406"/>
      </g>
    </g>

    <!-- external wheel -->
    <g class="wheel external" transform="translate(561 0)">
      <path d="M521.4 399.6 A212 212 0 1 0 182.6 399.6 L200.2 386.4 A190 190 0 1 1 503.8 386.4 Z" fill="var(--ring-black)"/>
      <circle cx="352" cy="272" r="190" fill="var(--navy)"/>
      <path d="M352 272 L196.4 163 A190 190 0 0 1 507.6 163 Z" fill="var(--ring-band)"/>
      <circle cx="352" cy="272" r="160" fill="var(--ring-mid)"/>
      <path d="M352 272 L250.7 330.5 A117 117 0 0 1 352 155 Z" fill="var(--slice-1)"/>
      <path d="M352 272 L352 155 A117 117 0 0 1 453.3 330.5 Z" fill="var(--slice-2)"/>
      <path d="M352 272 L453.3 330.5 A117 117 0 0 1 250.7 330.5 Z" fill="var(--slice-4)"/>
      <text class="ring-label small" x="352" y="81">Franchise Lawyers | Finance</text>
      <text class="ring-label small" x="352" y="92">Comittiee Members</text>
      <text class="ring-label" x="352" y="118">Legal Analysts</text>
      <text class="ring-label small" x="354" y="146">Phycisians, Clinicians</text>
      <text class="ring-label small" x="354" y="157">Scientists</text>
      <text class="ring-label" x="354" y="415">External Orgs</text>
      <g stroke="var(--white)" stroke-width="0.8">
        <line x1="424" y1="90" x2="433" y2="96"/>
        <line x1="392" y1="118" x2="401" y2="121"/>
        <line x1="296" y1="154" x2="303" y2="148"/>
      </g>
    </g>

    <!-- org chart connectors -->
    <g class="connectors" fill="none" stroke-width="1.2">
      <path d="M44 565 V751 H54 M44 636 H54 M174 565 V632 H182" stroke="var(--pink)"/>
      <path d="M498 565 V751 H509 M498 636 H509 M628 565 V632 H637 M485 653 V633 H498" stroke="var(--green)"/>
    </g>
    <line x1="22" y1="733" x2="740" y2="733" stroke="#555" stroke-width="1" stroke-dasharray="8 4"/>
  </svg>

  <div class="section-tag" style="left:30px">Internal</div>
  <div class="section-tag" style="left:605px">External</div>

  <!-- internal wheel boxes -->
  <div class="specialist" style="left:269px;top:217px"><div class="name">NBRX</div><div class="role">specialists</div><div class="scope">(Med products -<br>Commercial)</div></div>
  <div class="specialist" style="left:345px;top:217px"><div class="name">NBRX</div><div class="role">specialists</div><div class="scope">(Bio Science -<br>Commercial)</div></div>
  <div class="specialist" style="left:269px;top:287px"><div class="name">NBRX</div><div class="role">specialists</div><div class="scope">(Med products -<br>Med Affairs)</div></div>
  <div class="specialist" style="left:345px;top:287px"><div class="name">NBRX</div><div class="role">specialists</div><div class="scope">(Bio Science -<br>Med Affairs)</div></div>
  <div class="tag-box" style="left:345px;top:348px;width:46px">Clinical<br>Affairs</div>

  <div class="num" style="left:250px;top:218px">1</div>
  <div class="num" style="left:411px;top:218px">2</div>
  <div class="num" style="left:250px;top:288px">3</div>
  <div class="num" style="left:411px;top:288px">4</div>
  <div class="num" style="left:394px;top:350px">5</div>
  <div class="num" style="left:373px;top:399px">6</div>
  <div class="num" style="left:268px;top:153px">7</div>
  <div class="num" style="left:387px;top:117px">8</div>
  <div class="num" style="left:421px;top:92px">9</div>

  <!-- external wheel boxes -->
  <div class="specialist" style="left:837px;top:209px"><div class="name">NBRX</div><div class="role">specialists</div><div class="scope">(Med products -<br>Med Affairs)</div></div>
  <div class="specialist" style="left:929px;top:209px"><div class="name">NBRX</div><div class="role">specialists</div><div class="scope">(Bio Science -<br>Med Affairs)</div></div>
  <div class="specialist tall" style="left:883px;top:295px"><div class="name">NBRX</div><div class="role">specialists</div><div class="scope">(Contributions<br>Management<br>Programs)</div></div>

  <div class="num" style="left:882px;top:190px">10</div>
  <div class="num" style="left:929px;top:190px">11</div>
  <div class="num" style="left:949px;top:347px">12</div>
  <div class="num" style="left:848px;top:151px">13</div>
  <div class="num" style="left:962px;top:117px">14</div>
  <div class="num" style="left:994px;top:92px">15</div>

  <!-- org chart -->
  <div class="division medical" style="left:38px;top:514px">Medical Products</div>
  <div class="division bio" style="left:492px;top:514px">Bio Science</div>

  <div class="zone-label" style="left:314px;top:590px">Internal</div>
  <div class="zone-label" style="left:314px;top:760px">External</div>

  <div class="team pink" style="left:54px;top:626px"><div class="team-title">Medical Affairs</div><div class="team-members">Marian Hollis<br>Celia Vantner</div></div>
  <div class="team pink" style="left:182px;top:626px"><div class="team-title">Commercial</div><div class="team-members">Dora Pellman</div></div>
  <div class="team pink" style="left:54px;top:741px"><div class="team-title">Medical Affairs</div><div class="team-members">Kristin Ambler<br>Clara Wendt</div></div>

  <div class="team green" style="left:411px;top:653px;width:80px"><div class="team-title">Clinical Trials</div><div class="team-members" style="height:30px">Janet Corley</div></div>
  <div class="team green" style="left:509px;top:626px"><div class="team-title">Medical Affairs</div><div class="team-members">Ruben Castell</div></div>
  <div class="team green" style="left:637px;top:626px"><div class="team-title">Commercial</div><div class="team-members">Vera Latos<br>Noreen Blake</div></div>
  <div class="team green" style="left:509px;top:741px"><div class="team-title">Medical Affairs</div><div class="team-members">Mariam Qadri</div></div>

  <div class="team blue" style="left:254px;top:820px;width:176px"><div class="team-title">Contibutions Management team</div><div class="team-members">Annette Laird</div></div>

</div>
</body>
</html>
```